IT Consulting company Needs a Logo Design and Business Cards

I need a New Logo and Business Cards for an established IT Managed Services Company that specializes in flat-rate managed IT services. We provide Design and Build, Help Desk, Onsite and Remote Support Services.

Target Market(s)

Corporate Clients

Industry/Entity Type

It Company

Logo Text

Halvern Systems Collective

Requirements
Nice to have
• Tag Line= Support That Keeps Pace

```html
<!DOCTYPE html>
<html lang="en">
<head>
<meta charset="utf-8">
<title>Halvern Systems Collective – Business Card</title>
<link rel="stylesheet" href="https://fonts.googleapis.com/css2?family=Jost:wght@400;500;600&display=swap">
<style>
  :root {
    --backdrop: #1e1f21;
    --brand-blue: #233f8a;
    --card-white: #ffffff;
    --ink: #1d1d22;
    --on-blue: #ffffff;
  }
  * { box-sizing: border-box; margin: 0; padding: 0; }
  html, body { width: 1200px; height: 895px; overflow: hidden; }
  body {
    background: var(--backdrop);
    font-family: "Jost", "Futura", sans-serif;
    position: relative;
  }
  .card {
    position: absolute;
    width: 520px;
    height: 297px;
    box-shadow: 0 18px 40px rgba(0,0,0,.55);
  }
  .card--front {
    left: 70px; top: 130px;
    background: var(--brand-blue);
    color: var(--on-blue);
    display: flex; flex-direction: column; align-items: center; justify-content: center;
    text-align: center;
  }
  .card--back {
    left: 610px; top: 468px;
    background: var(--card-white);
    color: var(--ink);
    display: flex;
  }
  .wordmark {
    display: flex; align-items: center; gap: 14px;
    font-weight: 500;
    line-height: 1.15;
    letter-spacing: .05em;
    text-transform: uppercase;
    text-align: left;
  }
  .wordmark__text span { display: block; white-space: nowrap; }
  .wordmark__dot {
    border-radius: 50%;
    background: currentColor;
    flex: none;
  }
  .card--front .wordmark { font-size: 26px; }
  .card--front .wordmark__dot { width: 34px; height: 34px; }
  .tagline {
    font-size: 14px;
    font-weight: 500;
    letter-spacing: .02em;
    white-space: nowrap;
  }
  .card--front .tagline { margin-top: 40px; }
  .back__brand {
    width: 54%;
    padding-left: 32px;
    display: flex; flex-direction: column; justify-content: center; align-items: flex-start;
    color: var(--brand-blue);
  }
  .back__brand .wordmark { font-size: 18px; gap: 10px; }
  .back__brand .wordmark__dot { width: 26px; height: 26px; }
  .back__brand .tagline {
    margin-top: 22px;
    color: var(--ink);
    font-weight: 400;
    font-size: 13px;
  }
  .back__details {
    width: 46%;
    padding: 42px 18px 0 0;
    font-size: 12.5px;
    line-height: 1.45;
  }
  .person__name {
    color: var(--brand-blue);
    font-weight: 600;
    font-size: 18px;
    letter-spacing: .01em;
    text-transform: uppercase;
    white-space: nowrap;
  }
  .person__title { font-size: 13px; }
  .rule {
    width: 34px; height: 2px;
    background: var(--brand-blue);
    margin: 12px 0 10px;
  }
  .contact-list { list-style: none; }
  .contact-list li { display: flex; align-items: center; gap: 8px; white-space: nowrap; }
  .contact-list svg { width: 11px; height: 11px; fill: var(--brand-blue); flex: none; }
  .office__name { color: var(--brand-blue); font-size: 13.5px; white-space: nowrap; }
</style>
</head>
<body>
  <section class="card card--front" aria-label="Card front">
    <div class="wordmark">
      <span class="wordmark__dot"></span>
      <span class="wordmark__text"><span>Halvern</span><span>Systems Collective</span></span>
    </div>
    <p class="tagline">Support That Keeps Pace</p>
  </section>

  <section class="card card--back" aria-label="Card back">
    <div class="back__brand">
      <div class="wordmark">
        <span class="wordmark__dot"></span>
        <span class="wordmark__text"><span>Halvern</span><span>Systems Collective</span></span>
      </div>
      <p class="tagline">Support That Keeps Pace</p>
    </div>
    <div class="back__details">
      <h1 class="person__name">Marcus Delaney</h1>
      <p class="person__title">Founder &amp; CEO</p>
      <div class="rule"></div>
      <ul class="contact-list">
        <li><svg viewBox="0 0 24 24" aria-hidden="true"><path d="M6.6 10.8a15 15 0 0 0 6.6 6.6l2.2-2.2c.3-.3.7-.4 1-.2 1.1.4 2.3.6 3.6.6.6 0 1 .4 1 1V20c0 .6-.4 1-1 1A17 17 0 0 1 3 4c0-.6.4-1 1-1h3.5c.6 0 1 .4 1 1 0 1.2.2 2.4.6 3.6.1.3 0 .7-.2 1z"/></svg>+1 (555) 014 2260</li>
        <li><svg viewBox="0 0 24 24" aria-hidden="true"><path d="M2 5h20v14H2zM4 7v.5l8 5 8-5V7l-8 5z"/></svg>info@halvernsystems.com</li>
        <li><svg viewBox="0 0 24 24" aria-hidden="true"><path d="M12 2a10 10 0 1 0 0 20 10 10 0 0 0 0-20zm0 2c.9 1.2 1.6 2.6 2 4h-4c.4-1.4 1.1-2.8 2-4zM4.3 14a8 8 0 0 1 0-4h3.5a16 16 0 0 0 0 4zm5.5 0a14 14 0 0 1 0-4h4.4a14 14 0 0 1 0 4zm6.4 0a16 16 0 0 0 0-4h3.5a8 8 0 0 1 0 4zM12 20c-.9-1.2-1.6-2.6-2-4h4c-.4 1.4-1.1 2.8-2 4z"/></svg>www.halvernsystems.com</li>
      </ul>
      <div class="rule"></div>
      <p class="office__name">Halvern Systems Collective</p>
      <p>1842 Alder Row, Suite B</p>
      <p>Marlow Springs, CA 90418</p>
    </div>
  </section>
</body>
</html>
```